Stylized brand name and package design project for mini camera

We require a stylized version of our brand "Quorventil" (we call this a Logo) and we need a package design for our product.

We provide the package drawings (an Attached file named drawings)
This file is the old package design and is for you to get the dimensions only, please disregard all the elements and texts of this drawing.

We provide 3 product shots that need to be included in the package (see attached files named p1, p2, p3)
We provide a text file with the name of the product and the specs and phrases that need to be on the package. (the Attached file named brief)
We will provide a barcode that needs to be on the package (not attached yet)
See an example of a competing product (see the attached file named competitor)

Target Market(s)

18+ people concerned about the security of their homes, business, loved ones.

Font styles to use
Sans Serif

Colors
34a6d7
0493ce
85cae6
ffffff
6b449b

Requirements
Must have
• The elements on the brief (Logo, Products shots, text boxes)
• The main product shot should be the bigger centerpiece. with the other two products smaller.
Nice to have
• We would like to see a few backgrounds
• Products shots may (or may not) go inside white circles.

```html
<!DOCTYPE html>
<html lang="en">
<head>
<meta charset="utf-8">
<title>Quorventil Mini Camera – Package Options</title>
<link href="https://fonts.googleapis.com/css2?family=Montserrat:wght@300;400;500;600;700&display=swap" rel="stylesheet">
<style>
:root{
  --bg:#6e6e70;
  --bg-dark:#4d4d50;
  --blue:#1f9bd3;
  --blue-light:#34a6d7;
  --sky:#85cae6;
  --purple:#6b449b;
  --purple-deep:#5a2d97;
  --white:#ffffff;
  --paper:#f1f1f1;
  --paper-shade:#d9d9d9;
  --ink:#1c1c1c;
  --grey-text:#555;
  --device:#1a1a1a;
}
*{box-sizing:border-box;margin:0;padding:0}
html,body{width:900px;height:1200px;overflow:hidden}
body{
  position:relative;
  font-family:"Montserrat",sans-serif;
  background:radial-gradient(ellipse at 55% 40%,#7c7c7e 0%,var(--bg) 55%,var(--bg-dark) 100%);
}
.option-label{position:absolute;font-size:25px;font-weight:500;color:#000;letter-spacing:.5px}
.panel{position:absolute;overflow:hidden}
.flap-top{border-radius:16px 16px 0 0}
.flap-bottom{border-radius:0 0 16px 16px}
.paper{background:linear-gradient(160deg,var(--white) 0%,var(--paper) 55%,var(--paper-shade) 100%)}
.blue{background:var(--blue)}
.purple{background:linear-gradient(160deg,#7440b0 0%,var(--purple-deep) 60%,#4c2484 100%)}
.fold-line{position:absolute;left:0;right:0;height:1px;background:#bdbdbd}

.logo{position:absolute;left:0;right:0;text-align:center;font-weight:700;letter-spacing:1px;color:var(--ink)}
.logo.big{font-size:15px}
.logo.small{font-size:6.5px}
.logo.light{color:var(--white)}

.product-shot{position:absolute;border-radius:12px;background:radial-gradient(circle at 55% 50%,#5a2020 0%,#2a2a2a 28%,var(--device) 60%,#0c0c0c 100%)}
.accessory{position:absolute;border-radius:2px;background:linear-gradient(180deg,#3a3a3a,#111)}
.photo{position:absolute}

.title{position:absolute;font-weight:300;line-height:1}
.title .word{display:block;font-size:16px;color:#333}
.title .band{display:block;font-size:16px;padding:2px 4px}
.spec{position:absolute;font-size:6.5px;font-weight:500;color:var(--grey-text)}

.icon-row{position:absolute;display:flex;gap:4px}
.icon-col{position:absolute;left:0;right:0;display:flex;flex-direction:column;align-items:center;gap:13px}
.feature{display:flex;flex-direction:column;align-items:center;font-size:3.6px;font-weight:600;text-align:center;line-height:1.1;color:var(--ink)}
.feature svg{width:13px;height:13px;margin-bottom:2px}
.icon-col .feature{font-size:4.5px}
.icon-col .feature svg{width:16px;height:16px}
.on-dark .feature{color:var(--white)}

.contents{position:absolute;font-size:4.6px;line-height:1.35;color:var(--ink)}
.contents strong{display:block;font-size:5.4px;font-weight:700;margin-bottom:1px}
.on-dark .contents{color:var(--white)}
.plus{position:absolute;left:0;right:0;text-align:center;font-size:9px;color:var(--ink)}
.on-dark .plus{color:var(--white)}
</style>
</head>
<body>
<svg width="0" height="0" style="position:absolute" aria-hidden="true">
  <defs>
    <symbol id="frame" viewBox="0 0 20 20">
      <path d="M2 6V2h4M14 2h4v4M18 14v4h-4M6 18H2v-4" fill="none" stroke="currentColor" stroke-width="1.4"/>
    </symbol>
    <symbol id="ico-motion" viewBox="0 0 20 20">
      <use href="#frame"/><path d="M6 6l8 8M14 6l-8 8" stroke="currentColor" stroke-width="1.4"/>
    </symbol>
    <symbol id="ico-night" viewBox="0 0 20 20">
      <use href="#frame"/><circle cx="10" cy="10" r="4" fill="none" stroke="currentColor" stroke-width="1.4"/>
    </symbol>
    <symbol id="ico-video" viewBox="0 0 20 20">
      <use href="#frame"/><rect x="5" y="7" width="7" height="6" fill="none" stroke="currentColor" stroke-width="1.3"/><path d="M12 10l3-2v4z" fill="currentColor"/>
    </symbol>
    <symbol id="ico-picture" viewBox="0 0 20 20">
      <use href="#frame"/><rect x="5" y="6" width="10" height="8" fill="none" stroke="currentColor" stroke-width="1.3"/><circle cx="10" cy="10" r="2" fill="currentColor"/>
    </symbol>
  </defs>
</svg>

<!-- OPTION 1 -->
<div class="option-label" style="left:133px;top:230px">OPTION 1</div>
<section class="package option-one">
  <div class="panel paper flap-top" style="left:384px;top:45px;width:199px;height:108px"></div>

  <div class="panel blue on-dark" style="left:310px;top:152px;width:74px;height:203px">
    <div class="logo small light" style="top:28px">QUORVENTIL</div>
    <div class="icon-col" style="top:52px;color:#fff">
      <div class="feature"><svg><use href="#ico-motion"/></svg>MOTION DETECTION</div>
      <div class="feature"><svg><use href="#ico-night"/></svg>NIGHT VISION</div>
      <div class="feature"><svg><use href="#ico-video"/></svg>VIDEO</div>
      <div class="feature"><svg><use href="#ico-picture"/></svg>PICTURE</div>
    </div>
  </div>

  <div class="panel paper" style="left:384px;top:152px;width:199px;height:203px">
    <div class="logo big" style="top:22px">QUORVENTIL</div>
    <div class="product-shot" role="img" aria-label="Main mini camera product shot" style="left:8px;top:68px;width:88px;height:100px"></div>
    <div class="title" style="left:116px;top:108px;right:0">
      <span class="word">MINI</span>
      <span class="band" style="background:var(--blue);color:#fff;margin-left:-4px">CAMERA</span>
    </div>
    <div class="spec" style="left:116px;top:148px">FULL HD 1080P</div>
    <div class="icon-row" style="left:114px;top:172px;color:var(--ink)">
      <div class="feature"><svg><use href="#ico-motion"/></svg>MOTION<br>DETECTION</div>
      <div class="feature"><svg><use href="#ico-night"/></svg>NIGHT<br>VISION</div>
      <div class="feature"><svg><use href="#ico-video"/></svg>VIDEO</div>
      <div class="feature"><svg><use href="#ico-picture"/></svg>PICTURE</div>
    </div>
  </div>

  <div class="panel blue on-dark" style="left:583px;top:152px;width:77px;height:203px">
    <div class="logo small light" style="top:28px">QUORVENTIL</div>
    <div class="accessory" role="img" aria-label="Micro SD card reader" style="left:18px;top:60px;width:34px;height:14px"></div>
    <div class="plus" style="top:88px">+</div>
    <div class="accessory" role="img" aria-label="32GB micro SD card" style="left:22px;top:110px;width:24px;height:26px"></div>
    <div class="contents" style="left:10px;top:158px">
      <strong>PACKAGES CONTAINS:</strong>
      mini camera<br>micro SD card<br>micro SD card reader<br>mount bracket<br>mount clip<br>operating manual<br>USB charging / video out cable
    </div>
  </div>

  <div class="panel paper flap-bottom" style="left:660px;top:152px;width:200px;height:308px">
    <div class="logo big" style="top:22px">QUORVENTIL</div>
    <div class="product-shot" role="img" aria-label="Mini camera product shot" style="left:8px;top:68px;width:96px;height:100px"></div>
    <div class="title" style="left:122px;top:108px;right:0">
      <span class="word">MINI</span>
      <span class="band" style="background:var(--blue);color:#fff;margin-left:-4px">CAMERA</span>
    </div>
    <div class="spec" style="left:122px;top:148px">FULL HD 1080P</div>
    <div class="icon-row" style="left:120px;top:172px;color:var(--ink)">
      <div class="feature"><svg><use href="#ico-motion"/></svg>MOTION<br>DETECTION</div>
      <div class="feature"><svg><use href="#ico-night"/></svg>NIGHT<br>VISION</div>
      <div class="feature"><svg><use href="#ico-video"/></svg>VIDEO</div>
      <div class="feature"><svg><use href="#ico-picture"/></svg>PICTURE</div>
    </div>
    <div class="fold-line" style="top:278px"></div>
  </div>
</section>

<!-- OPTION 2 -->
<div class="option-label" style="left:617px;top:620px">OPTION 2</div>
<section class="package option-two">
  <div class="panel flap-top" style="left:104px;top:360px;width:199px;height:111px;background:var(--purple)">
    <svg width="199" height="111" style="position:absolute;inset:0" aria-hidden="true"><polygon points="70,0 199,0 199,111 150,111" fill="var(--blue-light)"/></svg>
  </div>

  <div class="panel paper" style="left:28px;top:470px;width:76px;height:202px">
    <div class="logo small" style="top:26px">QUORVENTIL</div>
    <div class="icon-col" style="top:44px;color:var(--ink)">
      <div class="feature"><svg><use href="#ico-motion"/></svg>MOTION DETECTION</div>
      <div class="feature"><svg><use href="#ico-night"/></svg>NIGHT VISION</div>
      <div class="feature"><svg><use href="#ico-video"/></svg>VIDEO</div>
      <div class="feature"><svg><use href="#ico-picture"/></svg>PICTURE</div>
    </div>
  </div>

  <div class="panel paper" style="left:104px;top:470px;width:199px;height:202px">
    <svg width="199" height="32" style="position:absolute;left:0;top:0" aria-hidden="true"><rect width="199" height="32" fill="var(--purple)"/><polygon points="150,0 199,0 199,32 120,32" fill="var(--blue-light)"/></svg>
    <div class="logo big light" style="top:9px;right:40px">QUORVENTIL</div>
    <div class="photo" role="img" aria-label="Night sky over calm water with a hot air balloon" style="left:0;top:32px;width:199px;height:92px;background:linear-gradient(180deg,#0c1424 0%,#1c2c4a 55%,#3a5878 72%,#16243c 100%)"></div>
    <div class="product-shot" role="img" aria-label="Mini camera product shot" style="left:5px;top:96px;width:76px;height:90px"></div>
    <div class="title" style="left:86px;top:154px;font-size:15px;font-weight:500;color:var(--blue)">MINI<span style="font-weight:300;color:#333">CAMERA</span></div>
    <div style="position:absolute;left:86px;top:172px;width:108px;height:1px;background:var(--blue)"></div>
    <div class="spec" style="left:90px;top:176px">FULL HD 1080P</div>
  </div>

  <div class="panel" style="left:303px;top:470px;width:75px;height:202px;background:linear-gradient(200deg,var(--blue-light) 0%,var(--blue-light) 42%,var(--paper) 42%,var(--paper) 100%)">
    <div class="logo small" style="top:26px">QUORVENTIL</div>
    <div class="accessory" role="img" aria-label="Micro SD card reader" style="left:16px;top:38px;width:36px;height:16px"></div>
    <div class="plus" style="top:76px">+</div>
    <div class="accessory" role="img" aria-label="32GB micro SD card" style="left:22px;top:104px;width:24px;height:26px"></div>
    <div class="contents" style="left:8px;top:152px">
      <strong>PACKAGES CONTAINS:</strong>
      mini camera<br>micro SD card<br>micro SD card reader<br>mount bracket<br>mount clip<br>operating manual<br>USB charging / video out cable
    </div>
  </div>

  <div class="panel paper flap-bottom" style="left:378px;top:470px;width:200px;height:310px">
    <svg width="200" height="32" style="position:absolute;left:0;top:0" aria-hidden="true"><rect width="200" height="32" fill="var(--purple)"/><polygon points="150,0 200,0 200,32 120,32" fill="var(--blue-light)"/></svg>
    <div class="logo big light" style="top:9px;right:40px">QUORVENTIL</div>
    <div class="photo" role="img" aria-label="Red vintage car parked on a warmly lit street" style="left:0;top:32px;width:200px;height:92px;background:linear-gradient(180deg,#4a3222 0%,#6b4a30 40%,#8a2a22 60%,#3a2a22 100%)"></div>
    <svg width="50" height="60" style="position:absolute;right:0;top:32px" aria-hidden="true"><polygon points="0,0 50,0 50,60" fill="var(--blue-light)"/></svg>
    <div class="product-shot" role="img" aria-label="Mini camera product shot" style="left:6px;top:96px;width:76px;height:90px"></div>
    <div class="title" style="left:86px;top:154px;font-size:15px;font-weight:500;color:var(--blue)">MINI<span style="font-weight:300;color:#333">CAMERA</span></div>
    <div style="position:absolute;left:86px;top:172px;width:108px;height:1px;background:var(--blue)"></div>
    <div class="spec" style="left:90px;top:176px">FULL HD 1080P</div>
    <div class="fold-line" style="top:280px"></div>
  </div>
</section>

<!-- OPTION 3 -->
<div class="option-label" style="left:630px;top:965px">OPTION 3</div>
<section class="package option-three">
  <div class="panel purple flap-top" style="left:125px;top:715px;width:203px;height:106px"></div>

  <div class="panel purple on-dark" style="left:48px;top:820px;width:77px;height:205px">
    <div class="logo small light" style="top:28px">QUORVENTIL</div>
    <div class="icon-col" style="top:52px;color:#fff">
      <div class="feature"><svg><use href="#ico-motion"/></svg>MOTION DETECTION</div>
      <div class="feature"><svg><use href="#ico-night"/></svg>NIGHT VISION</div>
      <div class="feature"><svg><use href="#ico-video"/></svg>VIDEO</div>
      <div class="feature"><svg><use href="#ico-picture"/></svg>PICTURE</div>
    </div>
  </div>

  <div class="panel purple on-dark" style="left:125px;top:820px;width:203px;height:205px">
    <div class="logo big light" style="top:24px">QUORVENTIL</div>
    <div class="product-shot" role="img" aria-label="Main mini camera product shot" style="left:6px;top:44px;width:108px;height:126px"></div>
    <div class="title" style="left:118px;top:112px;right:0">
      <span class="word" style="color:#fff">MINI</span>
      <span class="band" style="background:#fff;color:var(--purple);margin-left:-4px">CAMERA</span>
    </div>
    <div class="spec" style="left:120px;top:154px;color:#fff">FULL HD 1080P</div>
    <div class="icon-row" style="left:114px;top:176px;color:#fff">
      <div class="feature"><svg><use href="#ico-motion"/></svg>MOTION<br>DETECTION</div>
      <div class="feature"><svg><use href="#ico-night"/></svg>NIGHT<br>VISION</div>
      <div class="feature"><svg><use href="#ico-video"/></svg>VIDEO</div>
      <div class="feature"><svg><use href="#ico-picture"/></svg>PICTURE</div>
    </div>
  </div>

  <div class="panel" style="left:328px;top:825px;width:70px;height:200px;background:linear-gradient(90deg,var(--white) 0%,#e6e0ee 100%)">
    <div class="logo small" style="top:28px">QUORVENTIL</div>
    <div class="accessory" role="img" aria-label="Micro SD card reader" style="left:12px;top:56px;width:36px;height:16px"></div>
    <div class="plus" style="top:84px">+</div>
    <div class="accessory" role="img" aria-label="32GB micro SD card" style="left:16px;top:108px;width:24px;height:26px"></div>
    <div class="contents" style="left:6px;top:154px">
      <strong>PACKAGES CONTAINS:</strong>
      mini camera<br>micro SD card<br>micro SD card reader<br>mount bracket<br>mount clip<br>operating manual<br>USB charging / video out cable
    </div>
  </div>

  <div class="panel purple on-dark flap-bottom" style="left:398px;top:825px;width:204px;height:310px">
    <div class="logo big light" style="top:24px">QUORVENTIL</div>
    <div class="product-shot" role="img" aria-label="Mini camera product shot" style="left:8px;top:60px;width:102px;height:116px"></div>
    <div class="title" style="left:122px;top:112px;right:0">
      <span class="word" style="color:#fff">MINI</span>
      <span class="band" style="background:#fff;color:var(--purple);margin-left:-4px">CAMERA</span>
    </div>
    <div class="spec" style="left:124px;top:152px;color:#fff">FULL HD 1080P</div>
    <div class="icon-row" style="left:118px;top:176px;color:#fff">
      <div class="feature"><svg><use href="#ico-motion"/></svg>MOTION<br>DETECTION</div>
      <div class="feature"><svg><use href="#ico-night"/></svg>NIGHT<br>VISION</div>
      <div class="feature"><svg><use href="#ico-video"/></svg>VIDEO</div>
      <div class="feature"><svg><use href="#ico-picture"/></svg>PICTURE</div>
    </div>
    <div class="fold-line" style="top:280px;background:rgba(255,255,255,.35)"></div>
  </div>
</section>
</body>
</html>
```